New business Card Design

I'm looking to do a new design for our business cards.

Our Company its called the Lantern quarter we are a High end outdoor Design and construction company based out of miami FL

Our Style is elegant, minimalist, Luxury but accessible.

see our Website: www.thelanternquarter.example

Attached find our logo as well as some samples the cards that we have for our sister company.

Sample Contact information ( in no particular order):

Marco Bettancur
VP of Sales and Marketing
Marco@thelanternquarter.example
786.402.9158
4712 NW 63 AVE Miami Florida, 33166
Updates

Designs are Looking Great guys but not quite there yet!

Upload your last few designs between today and Tomorrow. we will be choosing one on Saturday!

Cheers, 

Marco Bettancur
Director Of Marketing 

Hello Guys, 

Sorry we have not made a decision yet.  a lot of cool stuff! just narrowing down our options. 
expect a decision with in a day or 2. 

Marco. 

Target Market(s)

high End Design and construction. Luxurious but accessible

Industry/Entity Type

Construction

Colors

Designer to choose colors to be used in the design.

```html
<!DOCTYPE html>
<html lang="en">
<head>
<meta charset="utf-8">
<title>The Lantern Quarter – Business Card</title>
<link rel="stylesheet" href="https://fonts.googleapis.com/css2?family=Questrial&display=swap">
<style>
  :root {
    --backdrop: #d9d9d6;
    --card: #ffffff;
    --ink: #2b2b2b;
    --muted: #555555;
    --blue: #1f78b4;
    --green: #5fa83a;
    --shadow: rgba(0, 0, 0, 0.22);
  }
  * { box-sizing: border-box; margin: 0; padding: 0; }
  html, body { width: 1200px; height: 871px; overflow: hidden; }
  body {
    background: var(--backdrop);
    font-family: "Questrial", "Century Gothic", sans-serif;
    color: var(--ink);
    position: relative;
  }
  .card {
    position: absolute;
    background: var(--card);
    box-shadow: 0 10px 28px var(--shadow);
    overflow: hidden;
  }
  /* Front */
  .card-front {
    left: 130px; top: 286px;
    width: 520px; height: 300px;
    background: linear-gradient(160deg, #ffffff 0%, #f1f1f1 55%, #dcdcdc 100%);
    display: flex; flex-direction: column; align-items: center; justify-content: center;
  }
  .brand-dot {
    width: 92px; height: 92px; border-radius: 50%;
    background: var(--blue);
    margin-bottom: 22px;
  }
  .brand-name {
    font-size: 34px; letter-spacing: 2px; text-transform: uppercase;
    color: var(--ink); line-height: 1;
  }
  .brand-tagline {
    margin-top: 6px;
    font-size: 15px; letter-spacing: 4.5px; text-transform: uppercase;
    color: var(--muted);
  }
  /* Back (portrait) */
  .card-back {
    left: 760px; top: 176px;
    width: 300px; height: 520px;
  }
  .contact {
    position: absolute; left: 34px; top: 44px; right: 30px;
  }
  .contact-name { font-size: 16px; font-weight: 700; letter-spacing: .5px; -webkit-text-stroke: .3px var(--ink); }
  .contact-role { font-size: 13px; color: var(--blue); margin-top: 6px; }
  .contact-address { font-size: 12px; color: var(--muted); margin-top: 16px; }
  .contact-list { list-style: none; margin-top: 22px; }
  .contact-list li {
    display: flex; justify-content: space-between; align-items: center;
    font-size: 12px; color: var(--muted); margin-bottom: 9px;
  }
  .contact-list svg { width: 11px; height: 11px; flex: none; }
  .back-circle {
    position: absolute; left: -70px; bottom: -70px;
    width: 300px; height: 300px; border-radius: 50%;
    background: var(--blue);
  }
</style>
</head>
<body>
  <section class="card card-front">
    <div class="brand-dot"></div>
    <div class="brand-name">The Lantern Quarter</div>
    <div class="brand-tagline">Innovation in Patio Design</div>
  </section>

  <section class="card card-back">
    <div class="contact">
      <div class="contact-name">Marco Bettancur</div>
      <div class="contact-role">VP of Sales and Marketing</div>
      <div class="contact-address">4712 NW 63 AVE Miami Florida, 33166</div>
      <ul class="contact-list">
        <li>786.402.9158
          <svg viewBox="0 0 12 12" aria-label="phone"><rect x="3" y="1" width="6" height="10" rx="1.2" fill="none" stroke="#5fa83a" stroke-width="1.4"/></svg>
        </li>
        <li>Marco@thelanternquarter.example
          <svg viewBox="0 0 12 12" aria-label="email"><rect x="1" y="2.5" width="10" height="7" fill="none" stroke="#5fa83a" stroke-width="1.3"/><path d="M1 2.5l5 4 5-4" fill="none" stroke="#5fa83a" stroke-width="1.3"/></svg>
        </li>
        <li>www.thelanternquarter.example
          <svg viewBox="0 0 12 12" aria-label="website"><circle cx="6" cy="6" r="4.8" fill="none" stroke="#5fa83a" stroke-width="1.3"/><path d="M1.2 6h9.6M6 1.2c-2.4 3-2.4 6.6 0 9.6M6 1.2c2.4 3 2.4 6.6 0 9.6" fill="none" stroke="#5fa83a" stroke-width="1"/></svg>
        </li>
      </ul>
    </div>
    <div class="back-circle"></div>
  </section>
</body>
</html>
```